Business Cards for Quenlow Massage and Wellness

I worked with designers from Pixel Harbor to make a wonderful logo and now I would like to use it in a business card. I have an intimate but progressive small clinical massage practice with far infrared sauna therapy for detox, vitasuction for pre and post surgery healing and ashiatsu and sports massage. We do lots of different modalities and I would like each therapist to have the same business card with their names on them. I would like to express our professionalism and connection to health.

I am attaching my logo and would like that included in the design. I love blues and greens. I would like something clean but creative, professional yet personality. I love the font copperplate gothic or I suppose whatever matches the logo. I would like to have the following information on the front of the card...

1. Logo

2. Address: Maplegate Square
5817 Tolvey Rd
Richmond, Va 23228
3. Phone: 804 555-0193

4. www.quenlowmassageandwellness.example

5. name of therapist, CMT (for example purposes Corin Battaway, CMT)

6. Optional information for front of card....
Far Infrared Sauna, Neuromuscular Therapy, VitaSuction, Detox Program, Deep Tissue, Swedish, Ashiatsu, Craniosacral Therapy, Reiki, Sports Massage, Couples Massage, Hot Stones, Cold Stones, LED Light Therapy

back of card...

1. Appointment Date/Time

2. Please provide 24 hours notice of cancellations

3. a line or space for appointment times.

```html
<!DOCTYPE html>
<html lang="en">
<head>
<meta charset="utf-8">
<title>Quenlow Massage and Wellness – Business Cards</title>
<link rel="stylesheet" href="https://fonts.googleapis.com/css2?family=Exo+2:wght@400;500&display=swap">
<style>
  :root {
    --page: #e9eaea;
    --card: #ffffff;
    --gold: #ab9a6e;
    --teal: #7fb5b0;
    --ink-light: #ffffff;
    --rule: #cfc4a6;
    --shadow: rgba(0, 0, 0, 0.18);
  }
  * { box-sizing: border-box; margin: 0; padding: 0; }
  html, body { width: 1200px; height: 898px; overflow: hidden; }
  body {
    background: var(--page);
    font-family: "Exo 2", Arial, sans-serif;
    position: relative;
  }
  .card {
    position: absolute;
    width: 620px;
    height: 354px;
    background: var(--card);
    box-shadow: 0 6px 18px var(--shadow);
    overflow: hidden;
  }
  .card--back { left: 290px; top: 46px; }
  .card--front { left: 290px; top: 498px; }

  .brand {
    display: flex;
    align-items: center;
    gap: 14px;
    color: var(--gold);
    font-weight: 400;
    letter-spacing: 0.04em;
  }
  .brand__dot { flex: none; border-radius: 50%; background: var(--teal); }
  .brand__name { line-height: 1.1; }

  /* Back: brand + appointment block */
  .card--back .brand {
    position: absolute;
    left: 50%; top: 44px;
    transform: translateX(-50%);
    font-size: 26px;
    white-space: nowrap;
  }
  .card--back .brand__dot { width: 40px; height: 40px; }

  .appointment {
    position: absolute;
    left: 70px; right: 70px; top: 132px;
    color: var(--gold);
  }
  .appointment__title {
    font-size: 14px;
    font-weight: 500;
    letter-spacing: 0.12em;
    text-transform: uppercase;
    text-align: center;
    margin-bottom: 18px;
  }
  .appointment__row {
    display: flex;
    align-items: flex-end;
    gap: 12px;
    font-size: 13px;
    letter-spacing: 0.05em;
    height: 34px;
  }
  .appointment__label { flex: none; width: 44px; }
  .appointment__line { flex: 1; border-bottom: 1px solid var(--rule); height: 1px; margin-bottom: 3px; }
  .appointment__note {
    margin-top: 26px;
    text-align: center;
    font-size: 12px;
    letter-spacing: 0.04em;
    color: var(--teal);
  }

  /* Front */
  .edge-strip {
    position: absolute;
    left: 0; top: 0;
    width: 12px; height: 100%;
    display: flex; flex-direction: column;
  }
  .edge-strip span:nth-child(1) { flex: 1; background: var(--gold); }
  .edge-strip span:nth-child(2) { flex: 1.4; background: var(--teal); }
  .edge-strip span:nth-child(3) { flex: 1.6; background: var(--gold); }

  .card--front .brand {
    position: absolute;
    left: 40px; top: 50%;
    transform: translateY(-50%);
    width: 250px;
    font-size: 24px;
  }
  .card--front .brand__dot { width: 38px; height: 38px; }

  .details {
    position: absolute;
    right: 0; top: 0;
    width: 300px; height: 100%;
    background: var(--gold);
    color: var(--ink-light);
    text-align: right;
    padding: 26px 22px 24px 16px;
    display: flex; flex-direction: column;
  }
  .details__name { font-size: 18px; font-weight: 500; letter-spacing: 0.05em; }
  .details__role { font-size: 12.5px; letter-spacing: 0.06em; margin-top: 4px; }
  .details__address { font-size: 13px; line-height: 1.55; margin-top: 34px; font-style: normal; }
  .details__contacts { list-style: none; margin-top: auto; font-size: 12px; line-height: 2; }
  .details__contacts li { display: flex; justify-content: flex-end; align-items: center; gap: 8px; white-space: nowrap; }
  .icon { flex: none; width: 12px; height: 12px; fill: none; stroke: var(--ink-light); stroke-width: 1.6; }
</style>
</head>
<body>

  <section class="card card--back" aria-label="Card back">
    <div class="brand">
      <span class="brand__dot"></span>
      <span class="brand__name">Quenlow Massage and Wellness</span>
    </div>

    <div class="appointment">
      <p class="appointment__title">Appointment</p>
      <div class="appointment__row"><span class="appointment__label">Date</span><span class="appointment__line"></span></div>
      <div class="appointment__row"><span class="appointment__label">Time</span><span class="appointment__line"></span></div>
      <p class="appointment__note">Please provide 24 hours notice of cancellations</p>
    </div>
  </section>

  <section class="card card--front" aria-label="Card front">
    <div class="edge-strip"><span></span><span></span><span></span></div>

    <div class="brand">
      <span class="brand__dot"></span>
      <span class="brand__name">Quenlow Massage and Wellness</span>
    </div>

    <div class="details">
      <p class="details__name">CORIN BATTAWAY, CMT</p>
      <p class="details__role">MASSAGE THERAPIST</p>
      <address class="details__address">Maplegate Square<br>5817 Tolvey Rd<br>Richmond, Va 23228</address>
      <ul class="details__contacts">
        <li>804 555-0193
          <svg class="icon" viewBox="0 0 12 12"><path d="M3 1.5 L4.6 4 L3.6 5 Q4.6 7.4 7 8.4 L8 7.4 L10.5 9 L9.5 10.8 Q4.5 10.5 1.2 2.5 Z"/></svg>
        </li>
        <li>www.quenlowmassageandwellness.example
          <svg class="icon" viewBox="0 0 12 12"><circle cx="6" cy="6" r="5"/><ellipse cx="6" cy="6" rx="2.2" ry="5"/><line x1="1" y1="6" x2="11" y2="6"/></svg>
        </li>
      </ul>
    </div>
  </section>

</body>
</html>
```